Business card for exciting VC company

Should look simple, crisp, and modern.

Industry/Entity Type

Venture Capital

Contact Information for Business Card

Would like to see at least one design that has our blue on the back with the tagline "Transforming Traditional Industry" and white front with contact details.

Font styles to use
Sans Serif

Requirements
Must have
• Logo

Darius Pellworth
dpellworth@brindlegate.vc
Managing Partner
M (628)304-xxxx

```html
<!DOCTYPE html>
<html lang="en">
<head>
<meta charset="utf-8">
<title>Brindlegate Capital – Business Card</title>
<link href="https://fonts.googleapis.com/css2?family=Lato:wght@400;700&display=swap" rel="stylesheet">
<style>
  :root {
    --brand-blue: #3f80c4;
    --ink: #141414;
    --paper: #ffffff;
    --backdrop: #e9eaec;
    --muted: #2a2a2a;
  }
  * { box-sizing: border-box; margin: 0; padding: 0; }
  html, body {
    width: 1200px; height: 847px; overflow: hidden;
    background: var(--backdrop);
    font-family: "Lato", sans-serif;
  }
  .sheet {
    width: 1200px; height: 847px;
    display: flex; align-items: center; justify-content: center; gap: 40px;
  }
  .card {
    position: relative;
    width: 540px; height: 309px;
    box-shadow: 0 6px 18px rgba(0,0,0,0.18);
  }
  .card--back { background: var(--brand-blue); }
  .card--front {
    background: var(--paper);
    border-bottom: 5px solid var(--brand-blue);
  }
  .wordmark {
    font-weight: 700;
    color: var(--ink);
    letter-spacing: 4px;
    text-transform: uppercase;
    line-height: 1;
    white-space: nowrap;
  }
  .card--back .wordmark {
    position: absolute; left: 0; right: 0; top: 118px;
    text-align: center; font-size: 30px;
  }
  .tagline {
    position: absolute; left: 34px; bottom: 30px;
    color: var(--paper);
    font-size: 13px; letter-spacing: 1.5px; text-transform: uppercase;
  }
  .card--front .wordmark {
    position: absolute; right: 34px; top: 40px;
    font-size: 22px;
  }
  .contact {
    position: absolute; left: 44px; top: 128px;
  }
  .contact__name {
    color: var(--brand-blue);
    font-weight: 700; font-size: 24px;
  }
  .contact__role {
    color: var(--muted); font-size: 14px; margin-top: 2px; margin-bottom: 16px;
  }
  .contact__list { list-style: none; }
  .contact__item {
    display: flex; align-items: center; gap: 10px;
    color: var(--ink); font-size: 15px; line-height: 25px;
  }
  .contact__icon { width: 14px; height: 14px; flex: none; }
</style>
</head>
<body>
<main class="sheet">
  <section class="card card--back" aria-label="Card back">
    <div class="wordmark">Brindlegate Capital</div>
    <p class="tagline">Transforming Traditional Industry</p>
  </section>

  <section class="card card--front" aria-label="Card front">
    <div class="wordmark">Brindlegate Capital</div>
    <div class="contact">
      <h1 class="contact__name">Darius Pellworth</h1>
      <p class="contact__role">Managing Partner</p>
      <ul class="contact__list">
        <li class="contact__item">
          <svg class="contact__icon" viewBox="0 0 24 24" aria-hidden="true"><path fill="#3f80c4" d="M6.6 10.8a15.1 15.1 0 0 0 6.6 6.6l2.2-2.2c.3-.3.7-.4 1-.2 1.1.4 2.3.6 3.6.6.6 0 1 .4 1 1V20c0 .6-.4 1-1 1A17 17 0 0 1 3 4c0-.6.4-1 1-1h3.5c.6 0 1 .4 1 1 0 1.3.2 2.5.6 3.6.1.3 0 .7-.2 1z"/></svg>
          (628)304-xxxx
        </li>
        <li class="contact__item">
          <svg class="contact__icon" viewBox="0 0 24 24" aria-hidden="true"><rect x="2" y="5" width="20" height="14" fill="#3f80c4"/><path d="M2 5l10 8 10-8" fill="none" stroke="#fff" stroke-width="1.6"/></svg>
          dpellworth@brindlegate.vc
        </li>
        <li class="contact__item">
          <svg class="contact__icon" viewBox="0 0 24 24" aria-hidden="true"><circle cx="12" cy="12" r="10" fill="none" stroke="#3f80c4" stroke-width="2"/><path d="M2 12h20M12 2c3 3 3 17 0 20M12 2c-3 3-3 17 0 20" fill="none" stroke="#3f80c4" stroke-width="1.5"/></svg>
          www.brindlegate.vc
        </li>
      </ul>
    </div>
  </section>
</main>
</body>
</html>
```